Custom unique Stationary design for Logistics company

We need a custom, unique , elegant and luxurious full stationary design using our new logo, following these guidelines:
1- Business card: double sided, both sides uses the navy blue as the background main color (same as the code of the navy blue used in our logo).
2- envelope and folder: also use the same navy blue as the main background color.
3- book cover( notepad cover) : same thing with the navy blue
4- letterhead: feel free to use the combination of the colors in our logo.
5- rest of the items are up to your creativity

Target Market(s)

corporates and other businesses

Industry/Entity Type

Logistics and heavy machines contractors

Requirements
Must have
• Letterhead, business card, envelope, notepad cover, paper, file
Nice to have
• navy blue to be main background color for business card, envelope, notepad cover

```html
<!DOCTYPE html>
<html lang="en">
<head>
<meta charset="utf-8">
<title>Northway Logistics – Presentation Folder</title>
<link href="https://fonts.googleapis.com/css2?family=Open+Sans:wght@400;600;700;800&display=swap" rel="stylesheet">
<style>
  :root {
    --stage: #6fa6e0;
    --navy: #27688a;
    --navy-deep: #1d5878;
    --orange: #f26b3a;
    --white: #ffffff;
    --logo-navy: #1f5a7a;
  }
  * { box-sizing: border-box; margin: 0; padding: 0; }
  html, body { width: 1200px; height: 847px; overflow: hidden; }
  body {
    background: var(--stage);
    font-family: "Open Sans", sans-serif;
    position: relative;
  }
  .folder {
    position: absolute;
    left: 60px; top: 44px;
    width: 1080px; height: 760px;
    display: flex;
    box-shadow: 0 12px 30px rgba(0,0,0,.25);
  }
  .panel {
    position: relative;
    width: 540px; height: 760px;
    background: linear-gradient(160deg, var(--navy) 0%, var(--navy-deep) 100%);
    overflow: hidden;
  }
  .panel--back { border-right: 1px solid rgba(0,0,0,.15); }
  .brand-name {
    position: absolute;
    color: var(--white);
    font-weight: 800;
    letter-spacing: 1px;
  }
  .panel--back .brand-name {
    top: 130px; left: 0; width: 540px;
    text-align: center;
    font-size: 40px;
  }
  .band {
    position: absolute;
    left: 0; width: 100%;
    background: var(--orange);
    padding: 18px 0;
  }
  .panel--back .band { top: 270px; }
  .panel--front .band { top: 200px; }
  .band__photo {
    height: 190px;
    background: linear-gradient(100deg, #2b4a6e 0%, #6f95bd 35%, #dbe8f4 55%, #7d9cbc 75%, #34506f 100%);
  }
  .badge {
    position: absolute;
    top: 160px; left: 120px;
    width: 300px; height: 300px;
    border-radius: 50%;
    background: radial-gradient(circle, #ffffff 55%, #eef2f5 100%);
    border: 14px solid var(--orange);
    display: flex; align-items: center; justify-content: center;
    text-align: center;
  }
  .badge .brand-name {
    position: static;
    color: var(--logo-navy);
    font-size: 34px;
    line-height: 1.15;
  }
  .contacts {
    position: absolute;
    left: 0; bottom: 70px; width: 540px;
    display: flex; justify-content: space-around; align-items: flex-start;
    padding: 0 20px;
  }
  .contact {
    display: flex; flex-direction: column; align-items: center;
    color: var(--white);
    font-size: 11px; font-weight: 600;
    text-align: center; line-height: 1.5;
  }
  .contact__icon {
    width: 40px; height: 40px; border-radius: 50%;
    background: var(--orange);
    display: flex; align-items: center; justify-content: center;
    margin-bottom: 12px;
  }
  .website {
    position: absolute;
    left: 0; width: 540px; bottom: 95px;
    text-align: center;
    color: var(--white);
    font-size: 20px; font-weight: 700;
  }
  .website-mark {
    position: absolute;
    left: 255px; bottom: 62px;
  }
</style>
</head>
<body>
  <div class="folder">
    <section class="panel panel--back">
      <div class="brand-name">Northway Logistics</div>
      <div class="band">
        <div class="band__photo" role="img" aria-label="Photo collage of a cargo ship, port cranes, an airplane and trucks linked by network icons"></div>
      </div>
      <div class="contacts">
        <div class="contact">
          <div class="contact__icon">
            <svg width="20" height="20" viewBox="0 0 20 20" fill="none" stroke="#fff" stroke-width="2.4"><circle cx="11" cy="8" r="5"/><line x1="7.5" y1="11.5" x2="3" y2="16" stroke-linecap="round"/></svg>
          </div>
          <span>www.northwaylogistics.com</span>
        </div>
        <div class="contact">
          <div class="contact__icon">
            <svg width="20" height="16" viewBox="0 0 20 16" fill="none" stroke="#fff" stroke-width="1.8"><rect x="1" y="2" width="18" height="12" rx="1"/><polyline points="1,2 10,9 19,2"/></svg>
          </div>
          <span>info@northwaylogistics.com<br>000-000-0000</span>
        </div>
        <div class="contact">
          <div class="contact__icon">
            <svg width="20" height="18" viewBox="0 0 20 18" fill="#fff"><polygon points="10,1 19,9 16,9 16,17 12,17 12,12 8,12 8,17 4,17 4,9 1,9"/></svg>
          </div>
          <span>14 Harbor Ave, NJ 000, United States</span>
        </div>
      </div>
    </section>

    <section class="panel panel--front">
      <div class="band">
        <div class="band__photo" role="img" aria-label="Photo collage of trucks, a cargo ship and port containers with network icons"></div>
      </div>
      <div class="badge">
        <div class="brand-name">Northway<br>Logistics</div>
      </div>
      <div class="website">northwaylogistics.com</div>
      <svg class="website-mark" width="30" height="14" viewBox="0 0 30 14"><polyline points="2,12 15,3 28,12" fill="none" stroke="#f26b3a" stroke-width="4"/></svg>
    </section>
  </div>
</body>
</html>
```